New Chartered Accounting Practice Needs Stationery Design

I need a new set of stationery including letterhead, business cards, envelopes and with compliments slips for a new Chartered Accounting Practice based in Melbourne, Victoria, Australia called "Martin K. Ashbury, Chartered Accountant".
I will be providing Taxation Services, Accounting Services, Self-Managed Superannuation Fund Consulting and general consulting advice to small and medium business enterprises. I would like to see designs that use the colour blue. The final design should communicate trust, technical expertise and security.
Target Market(s)
English speaking, Australians. Proprietors of small and medium businesses - aged 30-65. Fellow professionals - lawyers, investment consultants, other accountants. Retirees - aged 60 and over
Industry/Entity Type
Business
Look and feel

```html
<!DOCTYPE html>
<html lang="en">
<head>
<meta charset="utf-8">
<title>Martin K. Ashbury – Letterhead</title>
<link rel="stylesheet" href="https://fonts.googleapis.com/css2?family=Open+Sans:wght@400;600&family=Titillium+Web:wght@400;600&display=swap">
<style>
  :root {
    --backdrop: #ececec;
    --paper: #ffffff;
    --ink: #2b2b2b;
    --ink-soft: #6d6d6d;
    --blue-light: #b9dcee;
    --blue-mid: #4ea6d6;
    --blue-dark: #2c5ea8;
    --sign-area: #eef3f8;
  }
  * { box-sizing: border-box; margin: 0; padding: 0; }
  html, body { width: 1200px; height: 1000px; overflow: hidden; }
  body {
    background: var(--backdrop);
    font-family: "Open Sans", Arial, sans-serif;
    color: var(--ink);
  }
  .letterhead {
    position: absolute;
    left: 282px; top: 50px;
    width: 636px; height: 900px;
    background: var(--paper);
    box-shadow: 0 4px 18px rgba(0,0,0,.12);
    overflow: hidden;
  }
  .brand {
    position: absolute;
    top: 92px; left: 0; right: 0;
    display: flex; justify-content: center; align-items: center; gap: 12px;
  }
  .brand-square { width: 34px; height: 34px; background: var(--blue-mid); flex: none; }
  .brand-text { font-family: "Titillium Web", Arial, sans-serif; line-height: 1.1; }
  .brand-name { font-size: 21px; font-weight: 400; color: var(--ink); white-space: nowrap; }
  .brand-title { font-size: 13px; font-weight: 400; color: var(--ink); text-align: right; white-space: nowrap; }

  .letter-body {
    position: absolute;
    top: 190px; left: 74px; right: 74px;
    font-size: 8.6px; line-height: 1.55; color: var(--ink-soft);
  }
  .letter-body p { margin-bottom: 14px; }
  .letter-body .salutation { margin-bottom: 10px; }

  .signature {
    position: absolute;
    top: 560px; left: 330px;
    width: 150px; height: 44px;
    background: var(--sign-area);
  }

  .site-footer {
    position: absolute;
    left: 0; right: 0; bottom: 0;
  }
  .contact-bar {
    display: flex; justify-content: center; gap: 14px; align-items: center;
    padding: 0 30px 14px;
    font-size: 9px; color: var(--ink);
  }
  .contact-item { display: flex; align-items: center; gap: 4px; white-space: nowrap; }
  .contact-item svg { width: 9px; height: 9px; fill: var(--blue-dark); flex: none; }
  .footer-rule { height: 3px; background: var(--blue-light); }
  .footer-band { height: 12px; background: var(--blue-dark); }
</style>
</head>
<body>
<main class="letterhead">
  <header class="brand">
    <span class="brand-square"></span>
    <div class="brand-text">
      <div class="brand-name">Martin K. Ashbury</div>
      <div class="brand-title">Chartered Accountant</div>
    </div>
  </header>

  <section class="letter-body">
    <p class="salutation">Dear Client,</p>
    <p>Lorem ipsum dolor sit amet, consectetur adipiscing elit. Nulla sodales nisi vitae Lorem ipsum dolor sit amet, consectetur adipiscing elit. Suspendisse feugiat eros nisl, a facilisis risus eleifend sed. Aliquam mauris enim, fermentum eu lacinia sit amet, laoreet eu leo. Nullam eleifend nulla in libero tristique, ac vulputate odio tincidunt. Etiam non condimentum tortor. Integer suscipit neque nec odio porttitor cursus. Phasellus a sapien blandit, suscipit justo id, condimentum ante. Morbi tristique justo risus, id mattis dui molestie ut. Nullam volutpat ut quam commodo faucibus. Pellentesque urna est, interdum in elit quis, pharetra elementum orci. Nam pharetra velit molestie justo placerat scelerisque.</p>
    <p>Ut vitae interdum diam, in euismod ante. Pellentesque volutpat, risus sit amet sodales hendrerit, mi turpis vulputate dolor, eget cursus nulla eros nec tellus. Nulla tincidunt molestie libero vel pretium. Donec condimentum nulla sit amet risus semper imperdiet. Duis congue eros nec diam blandit, et pellentesque sapien auctor. Curabitur iaculis enim lectus, in imperdiet mauris mattis eget. Etiam ac ornare metus. Mauris risus leo, egestas at dolor a, ultrices adipiscing est. Nunc faucibus scelerisque mollis. Pellentesque aliquet mauris tellus, id dignissim risus viverra et. Mauris venenatis lobortis eros. Nam id diam in ligula malesuada feugiat. Cras turpis felis, aliquet id mauris elementum, feugiat ultricies nisl.</p>
    <p>Best regards,</p>
  </section>

  <div class="signature" role="img" aria-label="Handwritten signature of Martin Ashbury"></div>

  <footer class="site-footer">
    <div class="contact-bar">
      <span class="contact-item"><svg viewBox="0 0 10 10"><path d="M5 0a3.5 3.5 0 0 0-3.5 3.5C1.5 6 5 10 5 10s3.5-4 3.5-6.5A3.5 3.5 0 0 0 5 0zm0 5a1.5 1.5 0 1 1 0-3 1.5 1.5 0 0 1 0 3z"/></svg>PO Box 4410, Kew VIC 3101</span>
      <span class="contact-item"><svg viewBox="0 0 10 10"><path d="M2 0l2 2.5-1.2 1.2a6 6 0 0 0 3.5 3.5L7.5 6 10 8 8.5 10C4 10 0 6 0 1.5z"/></svg>0412 555 018</span>
      <span class="contact-item"><svg viewBox="0 0 10 10"><path d="M1 2h8v6H1z M2 3v1h6V3z"/></svg>(03) 9555 0142</span>
      <span class="contact-item"><svg viewBox="0 0 10 10"><path d="M0 2h10v1L5 6 0 3z M0 4l5 3 5-3v4H0z"/></svg>martin.ashbury@ashburyca.com.au</span>
    </div>
    <div class="footer-rule"></div>
    <div class="footer-band"></div>
  </footer>
</main>
</body>
</html>
```